Flyer for Fertility Specialty Pharmacy

We need to design a flyer , which contains the information about our Fertility Pharmacy , Services, and Medication pricing. We will be distributing these to Fertility clinics and Patients. We will provide the logo.
http://corvelmedrx.com/

Target Market(s)

Fertility Clinics , IVF patients, Other pharmacies

Industry/Entity Type

Fertility

Requirements
Must have
• baby pictures , or related to Fertility, IVF etc
Nice to have
• This flyer is to attract couples who are trying for pregnancy.

```html
<!DOCTYPE html>
<html lang="en">
<head>
<meta charset="utf-8">
<title>Corvel's Family Pharmacy – Fertility Trifold</title>
<link href="https://fonts.googleapis.com/css2?family=Saira:wght@300;400;500;700&display=swap" rel="stylesheet">
<style>
  :root {
    --teal: #00ad92;
    --teal-deep: #0a7f6c;
    --white: #ffffff;
    --ink: #4a4a4a;
    --backdrop: #4b4d4d;
    --photo-grey-light: #cfcfcf;
    --photo-grey-dark: #3c3c3c;
  }
  * { box-sizing: border-box; margin: 0; padding: 0; }
  html, body {
    width: 1200px; height: 900px; overflow: hidden;
    background: var(--backdrop);
    font-family: "Saira", sans-serif;
  }
  .sheet {
    position: absolute; left: 45px; top: 21px;
    width: 1110px; height: 858px;
    display: flex;
    box-shadow: 0 10px 40px rgba(0,0,0,.45);
  }
  .panel { position: relative; width: 370px; height: 100%; background: var(--white); overflow: hidden; }
  .band {
    position: absolute; left: 0; top: 0; width: 100%; height: 70px;
    display: flex; align-items: flex-end; justify-content: center; padding-bottom: 10px;
    font-size: 8.5px; letter-spacing: .08em; color: var(--white); text-transform: uppercase; font-weight: 300;
  }
  .band--teal { background: var(--teal); }
  .band--dark { background: linear-gradient(180deg, #1f1f1f, #6a6a6a); }

  /* Panel 1 */
  .intro { position: absolute; left: 48px; top: 104px; right: 36px; color: var(--ink); }
  .intro h2 { font-weight: 300; color: var(--teal); font-size: 27px; line-height: 1.1; margin-bottom: 4px; letter-spacing: .02em; }
  .intro p { font-size: 14px; line-height: 1.3; font-weight: 300; margin-bottom: 20px; letter-spacing: .02em; }
  .program {
    position: absolute; left: 0; top: 600px; width: 100%; bottom: 0;
    background: var(--teal); color: var(--white);
    display: flex; align-items: center; justify-content: center; text-align: center;
    font-size: 23px; font-weight: 300; line-height: 1.2; letter-spacing: .03em; padding: 0 10px;
    white-space: nowrap;
  }

  /* Panel 2 */
  .photo { position: absolute; left: 0; width: 100%; }
  .photo--green { top: 70px; height: 530px; background: radial-gradient(ellipse at 45% 60%, #2f9c85 0%, var(--teal-deep) 55%, #0b4f43 100%); }
  .contact {
    position: absolute; right: 40px; top: 150px; text-align: right; color: var(--white);
    font-size: 15px; line-height: 1.25; font-weight: 500; font-style: normal; letter-spacing: .02em;
  }
  .contact .lines { margin-top: 18px; font-size: 17px; }
  .lockup { display: flex; align-items: center; gap: 8px; color: var(--white); }
  .lockup__dot { width: 16px; height: 16px; border-radius: 50%; border: 2px solid var(--white); flex: none; }
  .lockup__name { font-weight: 500; font-size: 20px; line-height: 1; }
  .lockup__sub { font-weight: 500; font-size: 9px; }
  .lockup--small { position: absolute; left: 130px; top: 500px; }
  .shipping {
    position: absolute; left: 0; top: 600px; width: 100%; bottom: 0;
    display: flex; align-items: center; justify-content: center;
    color: var(--teal); font-weight: 700; font-size: 19px;
  }

  /* Panel 3 */
  .photo--grey { top: 70px; height: 530px; background: linear-gradient(160deg, var(--photo-grey-light) 0%, #9a9a9a 45%, var(--photo-grey-dark) 100%); }
  .tagline {
    position: absolute; left: 0; right: 0; top: 380px; text-align: center;
    color: var(--white); font-weight: 300; font-size: 32px; line-height: 1.15; letter-spacing: .04em;
  }
  .brand-block {
    position: absolute; left: 0; top: 600px; width: 100%; bottom: 0;
    background: var(--teal); display: flex; align-items: center; justify-content: center;
  }
  .brand-block .lockup__dot { width: 34px; height: 34px; border-width: 3px; }
  .brand-block .lockup { gap: 14px; }
  .brand-block .lockup__name { font-size: 38px; }
  .brand-block .lockup__sub { font-size: 15px; }
</style>
</head>
<body>
  <main class="sheet">
    <section class="panel panel--intro">
      <div class="band band--teal">Confidential pricing for Alpine Fertility Center</div>
      <div class="intro">
        <h2>Agnis quam</h2>
        <p>Agnis quam aut venditiis as aborum eatesto molo ex et aut laboressit aut que nimus magnate voluptae.</p>
        <p>To evene consedis maion re, sequi occus volo eum ipicatur magnien derchit, sedisitat quunt omnis aut as dolor magnis doluptur, aut idest estrum as quasimintia nem fuga.</p>
        <p>Itatemp orendae. Et volupta sitiatis errovid emporem quiatur andis imus quo blabori busciliquas dia consendipis derianimus ut por saeremos expersp elendiscius, abo.</p>
        <p>Bersper ibuscid ute eum in conessuntem quam evelestibusa cuptatas etur?</p>
      </div>
      <div class="program">We Are A Renew Rx &amp; Hope<br>Program</div>
    </section>

    <section class="panel panel--contact">
      <div class="band band--dark">Confidential pricing for Alpine Fertility Center</div>
      <div class="photo photo--green" role="img" aria-label="Teal-tinted close-up photo of a baby's hand holding an adult's finger"></div>
      <address class="contact">
        Corvel's Family Pharmacy<br>2240 Linden Ridge<br>Road Fairview, NJ 08512
        <div class="lines">Phone: 555-214-3380<br>Toll Free: 800-555-0147<br>Fax: 555-214-3391</div>
      </address>
      <div class="lockup lockup--small">
        <span class="lockup__dot"></span>
        <div><div class="lockup__name">Corvel's</div><div class="lockup__sub">Family Pharmacy</div></div>
      </div>
      <div class="shipping">Free SwiftPost Shipping</div>
    </section>

    <section class="panel panel--cover">
      <div class="band band--teal">Confidential pricing for Alpine Fertility Center</div>
      <div class="photo photo--grey" role="img" aria-label="Black and white photo of a newborn's hand gripping a parent's finger"></div>
      <h1 class="tagline">Certified Fertility<br>Specialists</h1>
      <div class="brand-block">
        <div class="lockup">
          <span class="lockup__dot"></span>
          <div><div class="lockup__name">Corvel's</div><div class="lockup__sub">Family Pharmacy</div></div>
        </div>
      </div>
    </section>
  </main>
</body>
</html>
```